Fresh & Clean *NEW* BUSINESS CARD Needed - OPTOMETRY Clinic/Optical

High-tech optometry practice with 3 doctors seeking new business card.  We provide eye exams, sell, designer glasses/contacts/specialty eyewear and treat ocular diseases.  For our business cards, we are seeking fresh, clean, and crisp design as we grow our team (staffing change).  Simply adding doctors is making the card look busy/cluttered.
 Looking for professional, less cluttered look yet still have our logo, doctor names, phone, address, and website....If possible!  :)
Names:
Marisol Pettigrew, O.D.
Ray Bellamy, O.D.
Nora Vantreese, O.D.
Phone: 555-214-6038
Website: www.BrightLensStudio.example
Address:  418 Harlan P. Moody, Fernhill, OR 70000
Ultimately we have the main business card with all doctor sames and that card has two versions  (front is always the same).  The back has two designs (1) displays next appointment time/date, (2) for "general use" (non-appointment.)    I have attached what we have used in the past.  
We also need a design template for each team member in our practice with their name, title, and email.   Those should be designed with the "general use" back (see attached).
**Open to entirely new design so don't feel obligated to keep current format.  Need new perspective!  Also including our watermark and some other design features we have consistently used in past in our portfolio.  Included are two options for logos--vertical and horizontal.
**I also would like to remove "Member of Optic Guild" on our logo if possible**
 Other image files available upon request.

Target Market(s)

New patient & Current Patients

Industry/Entity Type

Optometry

Contact Information for Business Card

High-tech optometry practice with 3 doctors seeking new business card.  We provide eye exams, sell, designer glasses/contacts/specialty eyewear and treat ocular diseases.  For our business cards, we are seeking fresh, clean, and crisp design as we grow our team (staffing change).  Simply adding doctors is making the card look busy/cluttered.  Looking for professional, less cluttered look yet still have our logo, doctor names, phone, address, and website....If possible!  :) Names: Marisol Pettigrew, O.D. Ray Bellamy, O.D. Nora Vantreese, O.D. Phone: 555-214-6038 Website: www.BrightLensStudio.example Address:  418 Harlan P. Moody, Fernhill, OR 70000 Ultimately we have the main business card with all doctor sames and that card has two versions  (front is always the same).  The back has two designs (1) displays next appointment time/date, (2) for "general use" (non-appointment.)    I have attached what we have used in the past.   We also need a design template for each team member in our practice with their name, title, and email.   Those should be designed with the "general use" back (see attached). **Open to entirely new design so don't feel obligated to keep current format.  Need new perspective!  Also including our watermark and some other design features we have consistently used in past in our portfolio.  Included are two options for logos--vertical and horizontal. **I also would like to remove "Member of Optic Guild" on our logo if possible**  Other image files available upon request.

Font styles to use
Other font styles liked:
• We have used Montserrat / Yellowtail in the past

Colors

Designer to choose colors to be used in the design.

Requirements
Must have
• Clean & Fresh Design with Logo / Info provided in description. Horizontal orientation. **I have included the CMYK colors we currently have in our logo.
Should not have
• Cluttered

```html
<!DOCTYPE html>
<html lang="en">
<head>
<meta charset="utf-8">
<title>BrightLens Studio – Business Card</title>
<link href="https://fonts.googleapis.com/css2?family=Quicksand:wght@400;500&family=Yellowtail&display=swap" rel="stylesheet">
<style>
  :root {
    --backdrop: #d9dde0;
    --card: #f3f3f3;
    --ink-grey: #5c5c60;
    --ink-slate: #3f5f73;
    --gold: #c9a21a;
    --aqua: #8ec8d6;
    --mark-faint: #e2e2e4;
    --mark-faint-inner: #e6eef1;
  }
  * { margin: 0; padding: 0; box-sizing: border-box; }
  html, body { width: 1200px; height: 900px; overflow: hidden; }
  body {
    background: var(--backdrop);
    font-family: "Quicksand", "Century Gothic", sans-serif;
    color: var(--ink-grey);
  }
  .stage {
    width: 1200px; height: 900px;
    display: flex; align-items: center; justify-content: center; gap: 50px;
  }
  .card {
    position: relative;
    width: 525px; height: 300px;
    background: var(--card);
    overflow: hidden;
    box-shadow: 0 6px 20px rgba(0,0,0,0.12);
  }
  .watermark {
    position: absolute;
    border-radius: 50%;
    background: var(--mark-faint-inner);
    border: 34px solid var(--mark-faint);
  }
  .card-front .watermark { width: 300px; height: 300px; right: -40px; top: -70px; }
  .card-back .watermark { width: 300px; height: 300px; right: -30px; top: -60px; }

  .brand {
    position: absolute;
    display: flex; align-items: center; gap: 10px;
    font-weight: 400; color: var(--ink-grey); white-space: nowrap;
  }
  .brand-dot {
    width: 34px; height: 34px; border-radius: 50%;
    background: var(--aqua); flex: none;
  }
  .card-front .brand { left: 26px; top: 70px; font-size: 30px; }

  .doctors {
    position: absolute; left: 26px; top: 144px;
    font-family: "Yellowtail", cursive; font-size: 20px; line-height: 1.2;
    color: var(--ink-slate); white-space: nowrap;
  }
  .rule {
    position: absolute; left: 100px; right: 18px; top: 184px;
    height: 1px; background: var(--gold);
  }
  .credential {
    position: absolute; left: 44px; top: 172px;
    font-family: "Yellowtail", cursive; font-size: 20px; line-height: 1.2;
    color: var(--gold);
  }
  .address {
    position: absolute; right: 26px; top: 196px;
    text-align: right; font-size: 14px; line-height: 1.3;
  }
  .contact {
    position: absolute; left: 42px; bottom: 20px;
    list-style: none; font-size: 14px; line-height: 1.6;
  }
  .contact li { display: flex; align-items: center; gap: 8px; }
  .contact svg { width: 14px; height: 14px; flex: none; }

  .card-back .brand-stack {
    position: absolute; left: 120px; top: 95px;
    display: flex; align-items: center; gap: 14px;
  }
  .card-back .brand-stack .brand-dot { width: 54px; height: 54px; }
  .card-back .brand-name {
    font-size: 44px; line-height: 1; color: var(--ink-grey); font-weight: 400;
  }
</style>
</head>
<body>
<main class="stage">
  <section class="card card-front" aria-label="Business card front">
    <div class="watermark" role="img" aria-label="Faint circular watermark"></div>
    <div class="brand"><span class="brand-dot"></span>BrightLens Studio</div>
    <p class="doctors">Marisol Pettigrew / Ray Bellamy / Nora Vantreese</p>
    <div class="rule"></div>
    <p class="credential">O.D.</p>
    <p class="address">418 Harlan P. Moody<br>Fernhill, OR 70000</p>
    <ul class="contact">
      <li>
        <svg viewBox="0 0 16 16" aria-hidden="true"><path d="M3 1.5l3 3-1.6 1.8a9 9 0 0 0 5.3 5.3L11.5 10l3 3-2 2C6.5 15 1 9.5 1 3.5z" fill="var(--gold)"/></svg>
        555-214-6038
      </li>
      <li>
        <svg viewBox="0 0 16 16" aria-hidden="true" fill="none" stroke="var(--gold)" stroke-width="1.2"><circle cx="8" cy="8" r="6.5"/><ellipse cx="8" cy="8" rx="3" ry="6.5"/><path d="M1.5 8h13M2.5 4.7h11M2.5 11.3h11"/></svg>
        www.BrightLensStudio.example
      </li>
    </ul>
  </section>

  <section class="card card-back" aria-label="Business card back">
    <div class="watermark" role="img" aria-label="Faint circular watermark"></div>
    <div class="brand-stack">
      <span class="brand-dot"></span>
      <p class="brand-name">BrightLens<br>Studio</p>
    </div>
  </section>
</main>
</body>
</html>
```